Medical Device - Case Study Template

We need a TEMPLATE that we can reuse to write various case studies about the medical equipment solutions we provide. It will be a double sided letter sized with a modern design that conveys a feeling of expertise, innovation and highly personable service AND be consistent with the brand guide. The content will be divided into a few sections:

- Situation (200-250 words)
- Challenge (100-120 words)
- Solution (100-120 words)
- Results (100-120 words)
- Conclusion (100-120 words)

Additionally, there will need to be a call to action, inviting people to send an email for more information and a short "About Valtu" section (approx. 40 words).

For device picture placeholders, feel free to use any random small benchtop medical device.

```html
<!DOCTYPE html>
<html lang="en">
<head>
<meta charset="utf-8">
<title>Valtu Medical Technology – Case Study Template</title>
<link href="https://fonts.googleapis.com/css2?family=Montserrat:wght@500;700;800&family=Roboto+Condensed:wght@300;400;500&display=swap" rel="stylesheet">
<style>
:root{
  --orange:#f58634;
  --steel:#7aa0bd;
  --steel-text:#5d89ad;
  --ink:#ffffff;
  --body:#4a4a4a;
  --backdrop:#e9ecef;
  --page:#ffffff;
}
*{box-sizing:border-box;margin:0;padding:0}
html,body{width:1200px;height:874px;overflow:hidden;background:var(--backdrop)}
body{position:relative;font-family:"Roboto Condensed",sans-serif}
.page{position:absolute;top:86px;width:496px;height:701px;background:var(--page);overflow:hidden;box-shadow:0 4px 14px rgba(0,0,0,.12)}
.page--front{left:88px}
.page--back{left:616px}
.abs{position:absolute}
.block-orange{background:var(--orange)}
.block-steel{background:var(--steel)}
.photo{border:3px solid #fff;background:linear-gradient(135deg,#eaf4fb 0%,#b9d6ec 45%,#6f9fc8 100%)}
.photo--wide{border:none;border-bottom:3px solid #fff;background:linear-gradient(90deg,#dbe8f3 0%,#9cbbd8 35%,#e3edf5 60%,#b4c6d6 100%)}
.title-box{color:var(--ink)}
.title-box .kicker{font-family:"Montserrat",sans-serif;font-weight:500;font-size:16px;border-top:1.5px solid #fff;border-bottom:1.5px solid #fff;padding:3px 2px 4px;width:176px;text-align:center;position:absolute;left:22px;top:48px}
.title-box h1{font-family:"Montserrat",sans-serif;font-weight:800;font-size:45px;line-height:44px;position:absolute;left:22px;top:86px;letter-spacing:-.5px}
.brand{font-family:"Montserrat",sans-serif;font-weight:700;color:var(--steel-text);display:flex;align-items:center;gap:10px}
.brand .dot{width:34px;height:34px;border-radius:50%;background:var(--orange);flex:none}
.brand .name{font-size:38px;line-height:1}
.brand-sub{font-family:"Montserrat",sans-serif;font-weight:500;color:var(--steel-text);letter-spacing:1px;white-space:nowrap}
.section-title{font-family:"Montserrat",sans-serif;font-weight:700;text-transform:uppercase}
.situation{color:#fff;padding:20px 22px 0 42px}
.situation h2{font-size:19px;margin-bottom:9px}
.situation p{font-size:7.4px;line-height:9.8px;font-weight:300;margin-bottom:10px}
.col{width:130px}
.col h2{font-size:16px;color:var(--orange);border-bottom:1.5px solid var(--orange);padding-bottom:2px;margin-bottom:9px}
.col p{font-size:7px;line-height:9.2px;color:var(--body);text-align:justify;margin-bottom:10px}
.conclusion{color:#fff;padding:12px 24px 0 24px}
.conclusion h2{font-size:17px;display:inline-block;border-bottom:1.5px solid #fff;padding-bottom:2px;margin-bottom:7px;padding-right:20px}
.conclusion p{font-size:7px;line-height:10px;font-weight:300;margin-bottom:10px}
.about h2{font-family:"Montserrat",sans-serif;font-weight:700;font-size:17px;color:var(--orange);display:inline-block;border-bottom:1.5px solid var(--orange);padding-bottom:1px;margin-bottom:6px}
.about p{font-size:8.6px;line-height:12px;color:var(--steel-text);font-weight:300;width:410px}
.footer-brand{width:172px}
.footer-brand .dot{width:26px;height:26px}
.footer-brand .name{font-size:28px}
.footer-brand .brand-sub{font-size:10px;letter-spacing:.6px;margin:5px 0 0 36px}
.contact{color:#fff;font-weight:500;font-size:11px;padding:10px 0 0 18px}
.contact .row{display:flex;align-items:center;gap:10px;height:19px}
.contact svg{width:14px;height:14px;flex:none}
</style>
</head>
<body>

<section class="page page--front">
  <div class="abs block-orange" style="left:0;top:0;width:250px;height:248px"></div>
  <div class="abs photo" role="img" aria-label="Photograph of a bright modern operating room with surgical lights and imaging equipment" style="left:30px;top:32px;width:444px;height:268px"></div>

  <div class="abs block-steel title-box" style="left:32px;top:302px;width:214px;height:189px">
    <div class="kicker">Medical Technology</div>
    <h1>CASE<br>STUDY</h1>
  </div>

  <div class="abs" style="left:282px;top:398px;width:164px;text-align:center">
    <div class="brand" style="justify-content:center"><span class="dot"></span><span class="name">Valtu</span></div>
    <div class="brand-sub" style="font-size:13px;margin-top:8px">Medical Technology</div>
  </div>

  <div class="abs block-steel" style="left:247px;top:551px;width:249px;height:150px"></div>
  <div class="abs block-orange situation" style="left:0;top:491px;width:470px;height:179px">
    <h2 class="section-title">Situation</h2>
    <p>Lorem ipsum dolor sit amet, consectetur adipiscing elit. Vivamus at nibh et tellus luctus placerat a eget magna. Etiam eu posuere dui. Cras tincidunt molestie lacus nec tristique. Aenean sed maximus lorem. In tempor mauris ligula, eu pulvinar mi cursus ut. Interdum et malesuada fames ac ante ipsum primis in faucibus. Integer iaculis vulputate elementum. Curabitur sapien velit, placerat id dolor sit amet, congue consequat nisl. Maecenas finibus ut lectus et molestie. Pellentesque et enim scelerisque, sagittis augue ut, accumsan diam. Donec in metus nec nibh varius maximus. Pellentesque ut egestas dolor. Mauris eu velit neque.</p>
    <p>Nunc id magna egestas, tincidunt diam in, molestie diam. Donec ac enim nunc. Nulla eget nisl id nulla tincidunt bibendum. Quisque aliquam sem ipsum, id fermentum sem semper ut. Quisque mollis, nisl ac pulvinar cursus, sapien lorem dignissim dui, sit amet vehicula nibh lacus quis nulla. Morbi sed tellus sollicitudin, ultricies turpis in, tincidunt magna. Pellentesque sed ante tortor. Morbi et lorem diam.</p>
    <p>Curabitur quis fringilla neque, at faucibus mi. Vestibulum faucibus ante quam, sit amet lacinia libero dictum sed. Donec sed tellus eget ante volutpat vehicula sed vitae elit. Aenean eleifend neque non sapien congue porta. Aenean vestibulum eros vel metus iaculis euismod.</p>
  </div>
</section>

<section class="page page--back">
  <div class="abs block-orange" style="left:246px;top:0;width:250px;height:211px"></div>
  <div class="abs photo photo--wide" role="img" aria-label="Photograph of a clinical equipment room with monitors, treatment table and device carts" style="left:0;top:34px;width:470px;height:150px"></div>

  <div class="abs col" style="left:36px;top:218px">
    <h2 class="section-title">Challenge</h2>
    <p>Lorem ipsum dolor sit amet, consectetur adipiscing elit. Integer pellentesque imperdiet metus. Nam auctor bibendum dapibus. Fusce ac posuere augue, ac finibus eros. Nullam gravida dui enim, vel molestie arcu vehicula sit amet. Vivamus metus dui, iaculis ut luctus nec, finibus non purus. Proin nisl ligula, rutrum vel augue at, ultricies sollicitudin risus. Morbi porta nibh vel porta mattis. Maecenas mauris metus, molestie at quam in, interdum blandit tellus. Fusce viverra consectetur dictum.</p>
    <p>Class aptent taciti sociosqu ad litora torquent per conubia nostra, per inceptos himenaeos. Vestibulum nec cursus sapien, ut tristique ligula. Nam non tincidunt nisl. Duis ac nibh.</p>
  </div>
  <div class="abs col" style="left:183px;top:218px">
    <h2 class="section-title">Solution</h2>
    <p>Lorem ipsum dolor sit amet, consectetur adipiscing elit. Integer pellentesque imperdiet metus. Nam auctor bibendum dapibus. Fusce ac posuere augue, ac finibus eros. Nullam gravida dui enim, vel molestie arcu vehicula sit amet. Vivamus metus dui, iaculis ut luctus nec, finibus non purus. Proin nisl ligula, rutrum vel augue at, ultricies sollicitudin risus. Morbi porta nibh vel porta mattis. Maecenas mauris metus, molestie at quam in, interdum blandit tellus. Fusce viverra consectetur dictum.</p>
    <p>Class aptent taciti sociosqu ad litora torquent per conubia nostra, per inceptos himenaeos. Vestibulum nec cursus sapien, ut tristique ligula. Nam non tincidunt nisl. Duis ac nibh.</p>
  </div>
  <div class="abs col" style="left:330px;top:218px">
    <h2 class="section-title">Results</h2>
    <p>Lorem ipsum dolor sit amet, consectetur adipiscing elit. Integer pellentesque imperdiet metus. Nam auctor bibendum dapibus. Fusce ac posuere augue, ac finibus eros. Nullam gravida dui enim, vel molestie arcu vehicula sit amet. Vivamus metus dui, iaculis ut luctus nec, finibus non purus. Proin nisl ligula, rutrum vel augue at, ultricies sollicitudin risus. Morbi porta nibh vel porta mattis. Maecenas mauris metus, molestie at quam in, interdum blandit tellus. Fusce viverra consectetur dictum.</p>
    <p>Class aptent taciti sociosqu ad litora torquent per conubia nostra, per inceptos himenaeos. Vestibulum nec cursus sapien, ut tristique ligula. Nam non tincidunt nisl. Duis ac nibh.</p>
  </div>

  <div class="abs block-orange conclusion" style="left:36px;top:410px;width:460px;height:114px">
    <h2 class="section-title">Conclusion</h2>
    <p>Lorem ipsum dolor sit amet, consectetur adipiscing elit. Integer pellentesque imperdiet metus. Nam auctor bibendum dapibus. Fusce ac posuere augue, ac finibus eros. Nullam gravida dui enim, vel molestie arcu vehicula sit amet. Vivamus metus dui, iaculis ut luctus nec, finibus non purus. Proin nisl ligula, rutrum vel augue at, ultricies sollicitudin risus. Morbi porta nibh vel porta mattis. Maecenas mauris metus, molestie at quam in, interdum blandit tellus. Fusce viverra consectetur dictum.</p>
    <p>Class aptent taciti sociosqu ad litora torquent per conubia nostra, per inceptos himenaeos. Vestibulum nec cursus sapien, ut tristique ligula. Nam non tincidunt nisl. Duis ac nibh.</p>
  </div>

  <div class="abs about" style="left:60px;top:535px">
    <h2>About Valtu</h2>
    <p>Lorem ipsum dolor sit amet, consectetur adipiscing elit. Nullam tortor urna, convallis at condimentum ac, malesuada interdum erat. Aliquam id urna viverra eros tristique iaculis et molestie ante. Nulla congue et metus at vestibulum. Donec facilisis dolor nec nulla mollis.</p>
  </div>

  <div class="abs footer-brand" style="left:36px;top:634px">
    <div class="brand"><span class="dot"></span><span class="name">Valtu</span></div>
    <div class="brand-sub">Medical Technology</div>
  </div>

  <div class="abs block-steel contact" style="left:218px;top:630px;width:278px;height:58px">
    <div class="row">
      <svg viewBox="0 0 24 24" fill="none" stroke="#fff" stroke-width="2" aria-hidden="true"><path d="M5 3h4l2 5-2.5 1.5a11 11 0 0 0 6 6L16 13l5 2v4a2 2 0 0 1-2 2A17 17 0 0 1 3 5a2 2 0 0 1 2-2z"/></svg>
      <span>55 210 384 9016 | 55 210 384 9016</span>
    </div>
    <div class="row">
      <svg viewBox="0 0 24 24" fill="none" stroke="#fff" stroke-width="2" aria-hidden="true"><rect x="3" y="5" width="18" height="14" rx="1"/><path d="M3 6l9 7 9-7"/></svg>
      <span>hello@valtumed.com | www.valtumed.com</span>
    </div>
  </div>
</section>

</body>
</html>
```